Martin Hale PA Card Logo

Current logo attached. Its 25 year old logo I have used. Looking for a new fresh elegant professional look/design for a law firm that has high net worth clientele and is estate planning business law firm. Firm mis in Palm Beach Florida.
One sided card linen stock white will be used. Logo section name section. Logo should include nice elegant design using the letter "M" perhapa (I am not wed to current font of the M on current logo.) Be creative there with logo design. My initials are MH.......color scheme I figure 3 tone... Raised Gold Foil, Blue name of firm = Martin Hale, P.A. My practice focus is Family and Business Asset Protection. My name is Martin M. Hale, Esq. Practice specialties include Asset Protection trusts, Business Succession Planning, LLC law, Estate Planning, Medicaid Planning (Maybe put those topics in bullets in a section of card. Bottom of card can be reserved smaller print address phone website and email address. Address section is not as important as logo and topics of practice on front. I foresee address section can be in dark blue. MY name and Topics dark blue as well.
Target Market(s)
affluent; business owners executives; wealth 2-10 million net worth
Industry/Entity Type
business law and estate planning
Contact Information for Business Card
White thick linen one sided

```html
<!DOCTYPE html>
<html lang="en">
<head>
<meta charset="utf-8">
<title>Martin Hale, P.A. — Business Card</title>
<link href="https://fonts.googleapis.com/css2?family=Montserrat:wght@400;700&family=Open+Sans:wght@400&family=PT+Sans+Narrow:wght@400&display=swap" rel="stylesheet">
<style>
  :root {
    --backdrop: #2b2b2d;
    --navy: #0b1f45;
    --ink: #0d1a3a;
    --gold: #d9a233;
    --gold-edge: #b8922a;
    --paper: #fbfbfa;
    --white: #f4f4f2;
  }
  * { margin: 0; padding: 0; box-sizing: border-box; }
  html, body {
    width: 1200px; height: 1160px; overflow: hidden;
    background: var(--backdrop);
  }
  .canvas { position: relative; width: 1200px; height: 1160px; }

  .card {
    position: absolute; left: 220px; width: 760px; height: 434px;
    border-bottom: 4px solid var(--gold-edge);
    box-shadow: 0 18px 40px rgba(0,0,0,.45);
  }
  .card--front { top: 96px; background: var(--navy); }
  .card--back  { top: 630px; background: var(--paper); }

  .brand { position: absolute; display: flex; align-items: center; gap: 26px; }
  .brand__mark { width: 110px; height: 110px; background: var(--gold); flex: none; }
  .brand__name {
    font-family: "Montserrat", sans-serif; font-weight: 400;
    font-size: 50px; line-height: 1.02; letter-spacing: 1px; text-transform: uppercase;
  }
  .brand__tagline {
    font-family: "Montserrat", sans-serif; font-weight: 400;
    font-size: 21px; line-height: 1.05; letter-spacing: 3px; text-transform: uppercase;
    margin-top: 8px;
  }

  .card--front .brand { left: 170px; top: 130px; }
  .card--front .brand__name { color: var(--white); }
  .card--front .brand__tagline { color: var(--gold); }

  .card--back .brand { left: 60px; top: 42px; }
  .card--back .brand__name { color: var(--ink); }
  .card--back .brand__tagline { color: var(--ink); font-size: 20px; }

  .contact { position: absolute; left: 60px; top: 260px; color: var(--ink); }
  .contact__name {
    font-family: "Montserrat", sans-serif; font-weight: 700; font-size: 30px;
    margin-bottom: 8px;
  }
  .contact__line {
    display: flex; align-items: center; gap: 10px;
    font-family: "Open Sans", sans-serif; font-size: 26px; line-height: 1.3;
  }
  .contact__icon { width: 20px; height: 20px; fill: var(--ink); flex: none; }

  .specialties {
    position: absolute; left: 440px; top: 282px; list-style: none;
    font-family: "PT Sans Narrow", sans-serif; font-size: 27px; line-height: 1.2;
    color: var(--ink);
  }
  .specialties li::before { content: "• "; }
</style>
</head>
<body>
<main class="canvas">

  <section class="card card--front" aria-label="Card front">
    <div class="brand">
      <span class="brand__mark" aria-hidden="true"></span>
      <div>
        <p class="brand__name">Martin<br>Hale, P.A.</p>
        <p class="brand__tagline">Family and Business<br>Asset Protection</p>
      </div>
    </div>
  </section>

  <section class="card card--back" aria-label="Card back">
    <div class="brand">
      <span class="brand__mark" aria-hidden="true"></span>
      <div>
        <p class="brand__name">Martin<br>Hale, P.A.</p>
        <p class="brand__tagline">Family and Business<br>Asset Protection</p>
      </div>
    </div>

    <div class="contact">
      <p class="contact__name">Martin M. Hale</p>
      <p class="contact__line">
        <svg class="contact__icon" viewBox="0 0 24 24" aria-hidden="true"><path d="M6.6 10.8a15.1 15.1 0 0 0 6.6 6.6l2.2-2.2c.3-.3.7-.4 1-.2 1.1.4 2.3.6 3.6.6.6 0 1 .4 1 1V20c0 .6-.4 1-1 1C10.6 21 3 13.4 3 4c0-.6.4-1 1-1h3.5c.6 0 1 .4 1 1 0 1.3.2 2.5.6 3.6.1.3 0 .7-.2 1z"/></svg>
        555-014-2876
      </p>
      <p class="contact__line">
        <svg class="contact__icon" viewBox="0 0 24 24" aria-hidden="true"><path d="M2 5h20v14H2z" fill="none"/><path d="M2 5h20v2l-10 6L2 7zM2 9l10 6 10-6v10H2z"/></svg>
        hale@harborestatelaw.com
      </p>
    </div>

    <ul class="specialties">
      <li>Asset Protection trusts</li>
      <li>Business Succession Planning</li>
      <li>LLC law, Estate Planning</li>
      <li>Medicaid Planning</li>
    </ul>
  </section>

</main>
</body>
</html>
```